Veterinary Power Point Template/Master

Dear Creatives,
we would need a Power Point Template that can be used for internal and external presentations. It'll mostly be needed to create B2B presentations at congresses or seminars, at which our vets attend as podium guests and lecturers.

What is important?
We see ourselves as highly professional, clean and innovative. One of our greatest mission is to build our work on latest medical research and the latest technology within veterinary medicine.
Therefore, our design should represent exactly this and look modern, professional and clinical.

Which slides do we need? What should they include?
- title
- section slides
- agenda
- Team slides to introduce our personell
- classic title & content
- slides to include different media and text options
- page numbers
- date
- our logo
- icons (if possible)

Unfortunately, we do not have an english version of our website yet, but feel free to browse through it to get a feeling for our appearance and values: https://www.tierpraxolan.at

We will also attach our little brand booklet as a guidance for you. BUT feel free to think out of the box and create a beautiful PPT design which is fun to watch.

Thrilled to see your great work already!

Target Market(s)

Austria

Industry/Entity Type

veterinary medicine

Font styles to use
Sans Serif
Other font styles liked:
• please only use Roboto font

Requirements
Must have
• items described in the creative brief
Nice to have
• animations and fancy transitions
Should not have
• Comic Sans or classic PPT Preset Designs

```html
<!DOCTYPE html>
<html lang="en">
<head>
<meta charset="utf-8">
<title>Tierpraxolan – Presentation Template</title>
<link href="https://fonts.googleapis.com/css2?family=Baloo+2:wght@600;700&family=Roboto:wght@400;500;700&display=swap" rel="stylesheet">
<style>
:root{
  --navy:#2b3544;
  --gold:#d9a900;
  --sheet:#e8e8e8;
  --white:#ffffff;
  --text:#3a3f47;
  --rule:#9aa0a8;
}
*{box-sizing:border-box;margin:0;padding:0}
html,body{width:1200px;height:4827px;overflow:hidden}
body{background:var(--sheet);font-family:"Roboto",sans-serif;color:var(--text);position:relative}
.slide{position:absolute;left:51px;width:1098px;height:617px;background:var(--white);overflow:hidden;box-shadow:0 2px 6px rgba(0,0,0,.08)}
.slide svg.shapes{position:absolute;inset:0;width:1098px;height:617px}
.photo{position:absolute}
.heading{position:absolute;font-family:"Baloo 2",sans-serif;font-weight:700;color:var(--navy);letter-spacing:.5px;line-height:1}
.page-tag{position:absolute;left:32px;top:22px;display:flex;align-items:center;gap:6px;font-size:12px;font-weight:700;color:var(--navy)}
.page-tag .num{width:32px;height:32px;border:2px solid var(--gold);border-radius:50%;display:flex;align-items:center;justify-content:center;font-size:13px}
.brand{position:absolute;display:flex;align-items:center;gap:8px}
.brand .dot{border-radius:50%;background:var(--navy);border:2px solid var(--gold)}
.brand .name{font-family:"Roboto",sans-serif;font-weight:700;color:var(--navy)}
.brand.small .dot{width:34px;height:34px}
.brand.small .name{font-size:15px}
.brand.large .dot{width:132px;height:132px;border-width:4px}
.brand.large .name{font-size:46px}
/* agenda */
.agenda-item{position:absolute;width:309px}
.agenda-item .row{display:flex;align-items:baseline;gap:14px;border-bottom:1.5px solid var(--rule);padding-bottom:8px}
.agenda-item .idx{font-family:"Baloo 2",sans-serif;font-weight:700;font-size:44px;line-height:.9;color:var(--gold)}
.agenda-item .label{font-size:13px;font-weight:700;color:var(--navy);text-transform:uppercase}
.agenda-item p{font-size:12.5px;line-height:22px;margin-top:10px;color:var(--text)}
/* body copy */
.copy{position:absolute;font-size:15px;line-height:31px;text-align:justify;color:var(--text)}
.copy p+p{margin-top:19px}
/* team */
.member{position:absolute;width:290px;text-align:center}
.member .portrait{position:relative;width:210px;height:210px;margin:0 auto}
.member .ring{position:absolute;left:0;top:0;width:210px;height:210px;border-radius:50%;background:var(--navy)}
.member .pic{position:absolute;left:12px;top:6px;width:190px;height:190px;border-radius:50%;background:radial-gradient(circle at 50% 40%,#f4f4f4,#9c9c9c 70%,#3c3c3c);border:3px solid var(--white)}
.member h3{font-size:15px;font-weight:700;color:var(--navy);margin-top:18px}
.member p{font-size:14.5px;line-height:23px;margin-top:10px;color:var(--text)}
.footer{position:absolute;top:4770px;left:52px;font-size:11px;color:var(--text)}
.thanks{position:absolute;left:0;width:1098px;text-align:center;top:318px;font-size:92px}
</style>
</head>
<body>

<!-- Title -->
<section class="slide" style="top:41px">
  <svg class="shapes" viewBox="0 0 1098 617">
    <path d="M0 0H485C525 0 525 55 485 85C430 125 395 110 350 160C300 215 240 190 190 260C145 325 95 395 0 440Z" fill="var(--gold)"/>
    <path d="M0 0H470C505 0 505 45 470 72C420 110 382 95 338 145C290 200 228 178 178 245C135 305 88 378 0 418Z" fill="var(--navy)"/>
    <path d="M815 0C770 60 800 135 778 205C752 290 728 365 748 435C765 505 715 570 670 617H1098V0Z" fill="var(--gold)"/>
  </svg>
  <svg class="photo" style="left:0;top:0" width="1098" height="617" viewBox="0 0 1098 617" role="img" aria-label="Smiling veterinarian with stethoscope holding a puppy">
    <defs><linearGradient id="g1" x1="0" y1="0" x2="1" y2="1"><stop offset="0" stop-color="#f1ece8"/><stop offset="1" stop-color="#c9b7aa"/></linearGradient></defs>
    <path d="M832 0C790 60 818 135 796 205C770 290 746 365 766 435C783 505 735 570 690 617H1098V0Z" fill="url(#g1)"/>
  </svg>
  <div class="photo" role="img" aria-label="Dog and cat looking upward" style="left:15px;top:400px;width:230px;height:217px;background:linear-gradient(135deg,#e6c9a4,#b6814e 60%,#d8cdbf);border-radius:40% 50% 0 0"></div>
  <div class="brand large" style="left:225px;top:142px"><span class="dot"></span><span class="name">Tierpraxolan</span></div>
  <h1 class="heading" style="left:145px;top:322px;font-size:42px">WELCOME TO TIERPRAXOLAN</h1>
</section>

<!-- Agenda -->
<section class="slide" style="top:716px">
  <svg class="shapes" viewBox="0 0 1098 617">
    <path d="M690 0H1098V440C1060 420 1020 440 1000 400C975 350 1010 300 990 255C965 205 900 220 865 180C830 140 870 100 800 80C740 60 700 40 690 0Z" fill="var(--navy)"/>
    <path d="M0 150C40 140 80 160 70 210C60 260 10 290 30 350C50 410 130 420 170 480C205 535 250 575 300 617H0Z" fill="var(--gold)"/>
  </svg>
  <div class="photo" role="img" aria-label="Small dog peeking in from the right edge" style="left:985px;top:385px;width:113px;height:232px;background:linear-gradient(160deg,#d89a55,#9a5a26);border-radius:50% 0 0 0"></div>
  <div class="page-tag"><span class="num">02</span>07/09/2023</div>
  <h2 class="heading" style="left:105px;top:82px;font-size:40px">AGENDA</h2>
  <div class="agenda-item" style="left:174px;top:150px"><div class="row"><span class="idx">01</span><span class="label">For pet owners</span></div><p>Lorem ipsum dolor sit amet, consectetur adipiscing elit,</p></div>
  <div class="agenda-item" style="left:518px;top:150px"><div class="row"><span class="idx">04</span><span class="label">Career</span></div><p>Lorem ipsum dolor sit amet, consectetur adipiscing elit,</p></div>
  <div class="agenda-item" style="left:174px;top:296px"><div class="row"><span class="idx">02</span><span class="label">For veterinarians</span></div><p>Lorem ipsum dolor sit amet, consectetur adipiscing elit,</p></div>
  <div class="agenda-item" style="left:518px;top:296px"><div class="row"><span class="idx">05</span><span class="label">Services</span></div><p>Lorem ipsum dolor sit amet, consectetur adipiscing elit,</p></div>
  <div class="agenda-item" style="left:174px;top:442px"><div class="row"><span class="idx">03</span><span class="label">For students</span></div><p>Lorem ipsum dolor sit amet, consectetur adipiscing elit,</p></div>
  <div class="agenda-item" style="left:518px;top:442px"><div class="row"><span class="idx">06</span><span class="label">Team</span></div><p>Lorem ipsum dolor sit amet, consectetur adipiscing elit,</p></div>
  <div class="brand small" style="left:904px;top:547px"><span class="dot"></span><span class="name">Tierpraxolan</span></div>
</section>

<!-- For veterinarians -->
<section class="slide" style="top:1388px">
  <svg class="shapes" viewBox="0 0 1098 617">
    <path d="M870 0H1098V617H1080C1060 560 1030 520 1040 470C1050 420 1020 380 1035 330C1050 270 1010 200 990 150C970 100 930 80 900 50C880 30 870 15 870 0Z" fill="var(--navy)"/>
    <path d="M0 280C40 285 60 330 60 380C60 440 110 480 170 530C220 575 280 600 300 617H0Z" fill="var(--gold)"/>
  </svg>
  <div class="photo" role="img" aria-label="Fluffy white puppy sitting" style="left:20px;top:400px;width:150px;height:175px;background:radial-gradient(circle at 50% 40%,#fbf7f1,#e0d5c4 70%,#c7b79f);border-radius:45%"></div>
  <div class="page-tag"><span class="num">03</span>07/09/2023</div>
  <h2 class="heading" style="left:102px;top:70px;font-size:40px">FOR VETERINARIANS</h2>
  <div class="copy" style="left:171px;top:134px;width:807px">
    <p>The Tierpraxolan sees itself as a specialist and referral clinic for dogs and cats. Our team specializes in the evaluation and treatment of complex illnesses and serious injuries. For this purpose, he has access to, among other things, a spacious operating center, various imaging procedures (e.g. endoscopy, CT, MRI) and an in-house laboratory.</p>
    <p>We see ourselves as a trustworthy and close partner of our referring veterinarians, who we support with our expertise, but also our medical technology and diagnostic options, as well as capacities for inpatient treatment (e.g. intensive care and isolation wards). In this way, we offer a useful addition to your range of services around the clock. The pet owner will be referred back to their family doctor for follow-up care and check-ups for the shared patients. Routine interventions such as vaccinations are not offered in the Tierpraxolan as a matter of principle.</p>
    <p>We are convinced that this concept creates the high degree of trust that is required for good cooperation on an equal footing between the referring veterinarian and the veterinary clinic</p>
  </div>
  <div class="brand small" style="left:900px;top:540px"><span class="dot"></span><span class="name">Tierpraxolan</span></div>
</section>

<!-- Team 1 -->
<section class="slide" style="top:2068px">
  <svg class="shapes" viewBox="0 0 1098 617">
    <path d="M640 0H1098V235C1070 220 1060 190 1030 180C990 165 960 190 930 160C900 130 930 95 890 80C850 65 790 80 740 65C690 50 650 30 640 0Z" fill="var(--gold)"/>
    <path d="M0 330C50 320 80 350 90 400C100 460 150 480 200 530C240 570 260 600 270 617H0Z" fill="var(--navy)"/>
    <circle cx="587" cy="63" r="21" fill="var(--gold)"/>
    <circle cx="1039" cy="384" r="41" fill="var(--navy)"/>
  </svg>
  <div class="page-tag"><span class="num">04</span>07/09/2023</div>
  <h2 class="heading" style="left:105px;top:68px;font-size:40px">TEAM</h2>
  <div class="member" style="left:108px;top:170px"><div class="portrait" role="img" aria-label="Portrait of Dr. Lukas Brenner"><span class="ring"></span><span class="pic"></span></div><h3>Dr. Lukas Brenner</h3><p>Diplomate ECVS, specialist in surgery, clinic manager, managing director</p></div>
  <div class="member" style="left:412px;top:170px"><div class="portrait" role="img" aria-label="Portrait of Dr Miriam Falk"><span class="ring"></span><span class="pic"></span></div><h3>Dr Miriam Falk</h3><p>Diplomate ECVIM-CA, specialist in internal medicine, clinic manager</p></div>
  <div class="member" style="left:704px;top:170px"><div class="portrait" role="img" aria-label="Portrait of Dr. Stefan Auer"><span class="ring"></span><span class="pic"></span></div><h3>Dr. Stefan Auer</h3><p>Specialist in internal medicine,<br>clinic manager</p></div>
  <div class="brand small" style="left:900px;top:540px"><span class="dot"></span><span class="name">Tierpraxolan</span></div>
</section>

<!-- Team 2 -->
<section class="slide" style="top:2747px">
  <svg class="shapes" viewBox="0 0 1098 617">
    <path d="M620 0H1098V25C1030 30 960 20 900 25C830 30 780 25 720 20C670 17 630 12 620 0Z" fill="var(--navy)"/>
    <path d="M0 370C50 360 90 400 100 460C110 520 160 560 230 590C270 605 300 612 320 617H0Z" fill="var(--gold)"/>
    <circle cx="851" cy="92" r="43" fill="var(--navy)"/>
    <circle cx="369" cy="564" r="21" fill="var(--gold)"/>
  </svg>
  <div class="page-tag"><span class="num">05</span>07/09/2023</div>
  <h2 class="heading" style="left:105px;top:68px;font-size:40px">TEAM</h2>
  <div class="member" style="left:108px;top:170px"><div class="portrait" role="img" aria-label="Portrait of Dr. Jonas Weidinger"><span class="ring"></span><span class="pic"></span></div><h3>Dr. Jonas Weidinger</h3><p>Diplomate ACVECC, specialist in emergency &amp; intensive care medicine, clinic manager</p></div>
  <div class="member" style="left:412px;top:170px"><div class="portrait" role="img" aria-label="Portrait of Mag. Petra Lindner-Moser"><span class="ring"></span><span class="pic"></span></div><h3>Mag. Petra Lindner-Moser</h3><p>Neurology, internal medicine, emergency &amp; intensive care medicine</p></div>
  <div class="member" style="left:704px;top:170px"><div class="portrait" role="img" aria-label="Portrait of Dr. Lena Marie Sandvik"><span class="ring"></span><span class="pic"></span></div><h3>Dr. Lena Marie Sandvik</h3><p>Surgery, emergency &amp;<br>intensive care medicine</p></div>
  <div class="brand small" style="left:904px;top:545px"><span class="dot"></span><span class="name">Tierpraxolan</span></div>
</section>

<!-- Cat friendly clinic -->
<section class="slide" style="top:3424px">
  <div class="page-tag"><span class="num">06</span>07/09/2023</div>
  <h2 class="heading" style="left:108px;top:88px;font-size:40px">CAT FRIENDLY CLINIC</h2>
  <div class="copy" style="left:161px;top:155px;width:806px">
    <p>The optimal care of our beloved four-legged friends also includes the sensitive handling of their fundamental emotions and fears. For this reason, the internationally recognized concepts of "cat-friendly" and "fear-free" were already taken into account when planning the Tierpraxolan. This means, among other things, that all of the stable areas mentioned above have strictly separate dog and cat departments, which are also separated from each other by noise protection walls. We want to make the visit to the veterinarian as pleasant as possible for even the most sensitive of our patients. Because people and animals should feel safe and in good hands during their entire stay in our veterinary clinic.</p>
  </div>
  <h2 class="heading" style="left:108px;top:413px;font-size:40px">24/7 EMERGENCY SERVICE AND SUPPORT</h2>
  <div class="copy" style="left:161px;top:481px;width:806px">
    <p>Of course, our patients are monitored and cared for around the clock by a veterinarian. A 24-hour emergency service is available to deal with unforeseen complaints and emergencies.</p>
  </div>
  <div class="brand small" style="left:904px;top:543px"><span class="dot"></span><span class="name">Tierpraxolan</span></div>
</section>

<!-- Thank you -->
<section class="slide" style="top:4118px">
  <svg class="shapes" viewBox="0 0 1098 617">
    <path d="M0 0H1098V250C1030 180 950 140 850 130C760 120 700 170 600 150C500 130 420 70 300 90C200 105 120 170 0 200Z" fill="var(--navy)"/>
    <path d="M0 470C120 520 200 500 300 470C420 430 520 470 620 490C760 520 900 430 1098 340V617H0Z" fill="var(--gold)"/>
    <circle cx="941" cy="354" r="35" fill="var(--navy)"/>
    <circle cx="126" cy="526" r="21" fill="var(--gold)"/>
  </svg>
  <div class="photo" role="img" aria-label="Puppy lying down resting its head" style="left:156px;top:430px;width:552px;height:187px;background:linear-gradient(90deg,rgba(255,255,255,0),#e9e4df 20%,#b9aaa0 45%,#e9e4df 75%,rgba(255,255,255,0))"></div>
  <div class="brand large" style="left:410px;top:180px;transform:scale(.72);transform-origin:left center"><span class="dot"></span><span class="name">Tierpraxolan</span></div>
  <h2 class="heading thanks">THANK YOU</h2>
</section>

<div class="footer">© 2023 TIERPRAXOLAN.</div>
</body>
</html>
```